Torvelin Business Card

We need a business card design. We have a logo from a previous PixelHarbor project and I am attaching the logo files in jpeg and photoshop.

Business

```html
<!DOCTYPE html>
<html lang="en">
<head>
<meta charset="utf-8">
<title>Torvelin Business Card</title>
<link rel="stylesheet" href="https://fonts.googleapis.com/css2?family=Mulish:wght@600;700;800&display=swap">
<style>
  :root {
    --backdrop: #d9d9d9;
    --card-white: #fbfbfb;
    --card-dark: #2b2b2b;
    --ink: #4a4a4a;
    --ink-soft: #5a5a5a;
    --brand-green: #4cb24f;
    --brand-grey: #5c5c5c;
  }
  * { margin: 0; padding: 0; box-sizing: border-box; }
  html, body {
    width: 1200px;
    height: 800px;
    overflow: hidden;
    background: var(--backdrop);
    font-family: "Mulish", "Century Gothic", sans-serif;
  }
  .stage {
    position: relative;
    width: 1200px;
    height: 800px;
    display: flex;
    align-items: center;
    justify-content: center;
    gap: 40px;
  }
  .card {
    position: relative;
    width: 520px;
    height: 297px;
    overflow: hidden;
    box-shadow: 0 6px 18px rgba(0,0,0,0.18);
  }

  /* Contact side */
  .card--contact { background: var(--card-white); }
  .contact-brand {
    position: absolute;
    top: 34px;
    right: 40px;
    display: flex;
    align-items: center;
    gap: 10px;
    font-size: 26px;
    font-weight: 800;
    color: var(--brand-grey);
  }
  .contact-brand__square {
    width: 22px;
    height: 22px;
    background: var(--brand-green);
  }
  .contact-details {
    position: absolute;
    left: 32px;
    top: 86px;
    color: var(--ink);
  }
  .person { position: relative; padding-left: 22px; }
  .person::before {
    content: "";
    position: absolute;
    left: 2px;
    top: 18px;
    width: 8px;
    height: 8px;
    background: var(--ink);
    transform: rotate(45deg);
  }
  .person__name {
    font-size: 19px;
    font-weight: 800;
    letter-spacing: 0.5px;
    color: var(--ink);
  }
  .person__role {
    font-size: 15px;
    font-weight: 700;
    color: var(--brand-green);
    margin-top: -2px;
  }
  .address {
    margin: 22px 0 0 40px;
    font-size: 14px;
    font-weight: 700;
    line-height: 1.2;
    color: var(--ink-soft);
  }
  .lines {
    list-style: none;
    margin: 12px 0 0 40px;
    font-size: 14px;
    font-weight: 700;
    line-height: 1.2;
    color: var(--ink-soft);
  }
  .lines__label { color: var(--brand-green); }
  .contact-band {
    position: absolute;
    left: 0;
    bottom: 0;
    width: 520px;
    height: 60px;
  }

  /* Brand side */
  .card--brand {
    background: var(--card-dark);
    display: flex;
    align-items: center;
    justify-content: center;
  }
  .brand-name {
    display: flex;
    align-items: center;
    gap: 14px;
    font-size: 54px;
    font-weight: 800;
    letter-spacing: -1px;
    color: var(--brand-green);
  }
  .brand-name__square {
    width: 40px;
    height: 40px;
    background: var(--brand-green);
  }
</style>
</head>
<body>
<main class="stage">
  <section class="card card--contact" aria-label="Contact side">
    <div class="contact-brand">
      <span class="contact-brand__square"></span>
      <span class="contact-brand__name">Torvelin</span>
    </div>
    <div class="contact-details">
      <div class="person">
        <p class="person__name">YOUR NAME</p>
        <p class="person__role">Company Position</p>
      </div>
      <address class="address" style="font-style:normal">
        111 Your Street Address<br>
        206 Town, CT 00000
      </address>
      <ul class="lines">
        <li><span class="lines__label">E:</span> youremail@domain.com</li>
        <li><span class="lines__label">P:</span> 111-222-444</li>
        <li><span class="lines__label">F:</span> 111-222-333</li>
      </ul>
    </div>
    <svg class="contact-band" viewBox="0 0 520 60" preserveAspectRatio="none" aria-hidden="true">
      <polygon points="0,22 520,4 520,14 0,32" fill="var(--brand-green)"/>
      <polygon points="0,36 520,18 520,60 0,60" fill="var(--brand-grey)"/>
    </svg>
  </section>

  <section class="card card--brand" aria-label="Brand side">
    <div class="brand-name">
      <span class="brand-name__square"></span>
      <span>Torvelin</span>
    </div>
  </section>
</main>
</body>
</html>
```